Industry automation wholesale website

www.velnora.eu provides solutions for automation, building automation and digital signage.

Our products are rugged, reliable, energy saving and representative.

Scope of pages:
● welcome page
- scope of products
- applications, success stories and news
● category page
- short introduction
- sub categories
- product highlights
● product page
- short introduction
- about 3 to 4 pictures
- technical specifications: materials, dimensions
- price
- related products

Optional:
● contact page
- address
- contact form
● blog
- picture
- text
● logo
● favicon / apple touch icon

Conclusion:
● We need a professionally looking site
● Bright colors (e.g. white, grey, metalic colors, blue)

some pages we like:
http://www.rubaskel.de/
http://www.parowind.de/

Target Market(s)

Our target market is the industrial sector
● Target audience: engineering and IT professionals

Industry/Entity Type

Building

Requirements
Must have
• ● only use free available fonts e.g. Lumivo Type Library (http://www.lumivotype.com/library)
Should not have
• ● sound
● flash

```html
<!DOCTYPE html>
<html lang="en">
<head>
<meta charset="utf-8">
<title>Velnora – Industrial Automation</title>
<link href="https://fonts.googleapis.com/css2?family=Arimo:ital,wght@0,400;0,700;1,400&family=Open+Sans:wght@300;400;600&display=swap" rel="stylesheet">
<style>
:root{
  --blue:#1f6e96;
  --blue-dark:#175a7c;
  --text:#555;
  --text-dark:#333;
  --line:#e2e2e2;
  --nav-bg:#f1f1f1;
  --footer:#1b1b1b;
  --white:#fff;
}
*{box-sizing:border-box;margin:0;padding:0}
html,body{width:860px;height:1200px;overflow:hidden;background:var(--white)}
body{position:relative;font-family:"Arimo",Arial,sans-serif;color:var(--text)}
a{color:inherit;text-decoration:none}

/* header */
.brand{position:absolute;left:62px;top:36px}
.brand-name{font-family:"Open Sans",sans-serif;font-weight:400;font-size:44px;line-height:44px;color:var(--blue);letter-spacing:1px;display:flex;align-items:center;gap:8px}
.brand-dot{width:10px;height:10px;background:var(--blue);border-radius:50%}
.brand-tag{font-size:11px;color:var(--blue);margin-top:2px}
.search{position:absolute;left:500px;top:30px;width:187px;height:26px;border:1px solid #d6d6d6;font-size:11px;color:#999;padding:7px 9px}
.search svg{position:absolute;right:7px;top:7px}
.lang{position:absolute;left:703px;top:30px;width:94px;height:26px;border:1px solid #d6d6d6;background:#f6f6f6;font-size:11px;color:var(--text-dark);display:flex;align-items:center;justify-content:center;gap:7px}
.lang-flag{width:22px;height:12px;background:linear-gradient(#3b4f8a,#2a3d75);border:1px solid #c22}
.contact-line{position:absolute;top:77px;font-size:11px;color:var(--text-dark);display:flex;align-items:center;gap:7px}
.contact-phone{left:590px}
.contact-mail{left:699px}

/* nav */
.nav{position:absolute;left:62px;top:113px;width:735px;height:40px;background:var(--nav-bg);border-bottom:3px solid var(--blue);display:flex}
.nav a{font-size:12.5px;color:var(--text-dark);padding:0 22px;line-height:37px;position:relative}
.nav a+a::before{content:"";position:absolute;left:0;top:13px;height:12px;border-left:1px dotted #aaa}
.nav a.active{background:var(--blue);color:var(--white);padding:0 16px}

/* slider */
.slider{position:absolute;left:62px;top:159px;width:735px;height:311px;background:radial-gradient(ellipse at 35% 45%,#2a1f08 0%,#0b0b0b 60%,#000 100%);overflow:hidden}
.slider-product{position:absolute;left:412px;top:42px;width:236px;height:230px;border-radius:26px;background:linear-gradient(135deg,#f4f4f4,#d8d8d8)}
.slider-text{position:absolute;left:47px;top:84px;color:var(--white);font-family:"Open Sans",sans-serif}
.slider-text h1{font-weight:600;font-size:26px;line-height:30px}
.slider-text h2{font-weight:300;font-size:21px;margin-top:6px}
.slider-text p{font-size:11px;line-height:20.5px;width:315px;margin-top:10px}
.dots{position:absolute;left:47px;top:243px;display:flex;gap:2px}
.dots span{width:8px;height:8px;border:1px solid #bbb;border-radius:50%}
.dots span:first-child{background:#ddd}

/* feature cards */
.card{position:absolute;top:503px;width:222px}
.card-photo{height:118px;border:1px solid var(--line);padding:5px;box-shadow:0 1px 3px rgba(0,0,0,.08)}
.card-photo div{width:100%;height:100%}
.card h3{font-weight:400;font-size:14px;color:var(--blue-dark);margin-top:12px}
.card p{font-size:10px;line-height:17.2px;margin-top:7px}
.btn{display:inline-block;margin-top:15px;background:var(--blue);color:var(--white);font-size:10.5px;padding:0 7px;line-height:22px}

/* sidebar */
.side{position:absolute;left:63px;top:801px;width:197px;box-shadow:0 1px 3px rgba(0,0,0,.12)}
.side a{display:flex;justify-content:space-between;align-items:center;height:34.4px;padding:0 12px 0 22px;font-size:11.5px;color:#444;border-bottom:1px solid #ececec;background:linear-gradient(90deg,#fff,#f5fafc)}
.side a.active{background:var(--blue);color:var(--white);font-size:13.5px;height:34px}
.side .arrow{width:18px;height:18px;border:1px solid #ddd;border-radius:50%;display:flex;align-items:center;justify-content:center;background:#fff}
.side a.active .arrow{background:#222;border-color:#fff}

/* content */
.section-title{position:absolute;left:303px;font-size:12.5px;color:var(--blue);letter-spacing:.4px}
.welcome{position:absolute;left:302px;top:830px;width:497px;font-size:9.8px;line-height:17.2px;color:var(--text-dark)}
.welcome p+p{margin-top:7px}
.quote{position:absolute;top:977px;width:235px;height:70px;background:#f1f1f1;font-style:italic;font-size:9.6px;line-height:17.2px;color:#444;padding:9px 0 0 16px}
.quote::before{content:"\201C";position:absolute;left:5px;top:2px;font-size:18px;color:#bbb}
.quote::after{content:"";position:absolute;left:135px;bottom:-9px;border-left:9px solid transparent;border-right:9px solid transparent;border-top:9px solid #f1f1f1}
.author{position:absolute;top:1065px;font-size:10px;color:var(--text-dark);display:flex;align-items:center;gap:6px}

/* footer */
.footer{position:absolute;left:0;top:1118px;width:860px;height:82px;background:var(--footer);color:#eee;font-size:10px}
.footer-links{position:absolute;left:62px;top:21px}
.footer-copy{position:absolute;left:62px;top:46px}
.social{position:absolute;left:616px;top:31px;display:flex;gap:9px}
.social span{width:25px;height:25px}
</style>
</head>
<body>

<header>
  <div class="brand">
    <div class="brand-name">velnora<span class="brand-dot"></span></div>
    <div class="brand-tag">analog digital measurements</div>
  </div>
  <div class="search">Search..
    <svg width="10" height="10" viewBox="0 0 10 10"><circle cx="4" cy="4" r="3" fill="none" stroke="#999" stroke-width="1.3"/><line x1="6.2" y1="6.2" x2="9.3" y2="9.3" stroke="#999" stroke-width="1.4"/></svg>
  </div>
  <div class="lang"><span class="lang-flag"></span>ENGLISH</div>
  <div class="contact-line contact-phone">
    <svg width="10" height="14" viewBox="0 0 10 14"><path d="M3 1 L6 1 L5 4 L3.5 4 Q3 7 4.5 10 L6 10 L7 13 L4 13 Q0 7 3 1Z" fill="#777"/></svg>555-214-0870
  </div>
  <div class="contact-line contact-mail">
    <svg width="14" height="10" viewBox="0 0 14 10"><rect x=".5" y=".5" width="13" height="9" fill="none" stroke="#777"/><path d="M.5 .5 L7 6 L13.5 .5" fill="none" stroke="#777"/></svg>info@velnora.de
  </div>
</header>

<nav class="nav">
  <a class="active" href="#">HOME</a>
  <a href="#">ABOUT US</a>
  <a href="#">PRODUCTS</a>
  <a href="#">CONTACT</a>
  <a href="#">SHOPPING CART</a>
</nav>

<section class="slider" role="img" aria-label="Oscilloscope waveform on a dark grid behind a white digital clock display">
  <div class="slider-product" role="img" aria-label="White digital display device showing time"></div>
  <div class="slider-text">
    <h1>Touch Panel PC</h1>
    <h2>Duis autem vel eum iriure dolor</h2>
    <p>Ut wisi enim ad minim veniam, quis nostrud exerci tation ullamcor per suscipit lobortis nisl ut aliquip ex ea commodo consequat. Dus autem vel eum iriure dolor.</p>
  </div>
  <div class="dots"><span></span><span></span><span></span><span></span></div>
</section>

<article class="card" style="left:62px">
  <div class="card-photo"><div role="img" aria-label="Row of blue serial converter modules" style="background:linear-gradient(135deg,#3e6fa8,#8aa6c4 60%,#a9b9c9)"></div></div>
  <h3>Modbus RTU / RS485 Remote</h3>
  <p>Claritas est etiam processus dynamicus, qui seq uitur mutationem consuetudium lecitorum.Mires t notare quam littera gothica, quam. Claritas.</p>
  <a class="btn" href="#">READ MORE</a>
</article>
<article class="card" style="left:319px">
  <div class="card-photo"><div role="img" aria-label="Technician using a rugged industrial touch panel" style="background:linear-gradient(90deg,#5a6a5f,#7d9a88 50%,#3f7aa0)"></div></div>
  <h3>Touch Panel Industry Computer</h3>
  <p>Claritas est etiam processus dynamicus, qui seq uitur mutationem consuetudium lecitorum.Mirus t notare quam littera gothica, quam. Claritas.</p>
  <a class="btn" href="#">READ MORE</a>
</article>
<article class="card" style="left:576px">
  <div class="card-photo"><div role="img" aria-label="Close-up of a blue printed circuit board with a chip" style="background:linear-gradient(135deg,#0e2a5c,#4d7cc0 55%,#16336a)"></div></div>
  <h3>Embedded systems for industrial</h3>
  <p>Claritas est etiam processus dynamicus, qui seq uitur mutationem consuetudium lectorum.Mirus t notare quam littera gothica, quam. Claritas.</p>
  <a class="btn" href="#">READ MORE</a>
</article>

<aside class="side">
  <a class="active" href="#">RS 422 Converter<span class="arrow"><svg width="6" height="6" viewBox="0 0 6 6"><path d="M0 3H5M3 1L5 3L3 5" fill="none" stroke="#fff"/></svg></span></a>
  <a href="#">RS422 Repeater<span class="arrow"><svg width="6" height="6" viewBox="0 0 6 6"><path d="M0 3H5M3 1L5 3L3 5" fill="none" stroke="#666"/></svg></span></a>
  <a href="#">RS485 Remote IO<span class="arrow"><svg width="6" height="6" viewBox="0 0 6 6"><path d="M0 3H5M3 1L5 3L3 5" fill="none" stroke="#666"/></svg></span></a>
  <a href="#">RS485 Modbus IO<span class="arrow"><svg width="6" height="6" viewBox="0 0 6 6"><path d="M0 3H5M3 1L5 3L3 5" fill="none" stroke="#666"/></svg></span></a>
  <a href="#">Embedded Systems<span class="arrow"><svg width="6" height="6" viewBox="0 0 6 6"><path d="M0 3H5M3 1L5 3L3 5" fill="none" stroke="#666"/></svg></span></a>
  <a href="#">PCI-Series<span class="arrow"><svg width="6" height="6" viewBox="0 0 6 6"><path d="M0 3H5M3 1L5 3L3 5" fill="none" stroke="#666"/></svg></span></a>
  <a href="#">Industry PC<span class="arrow"><svg width="6" height="6" viewBox="0 0 6 6"><path d="M0 3H5M3 1L5 3L3 5" fill="none" stroke="#666"/></svg></span></a>
  <a href="#">Industrial Display<span class="arrow"><svg width="6" height="6" viewBox="0 0 6 6"><path d="M0 3H5M3 1L5 3L3 5" fill="none" stroke="#666"/></svg></span></a>
</aside>

<h2 class="section-title" style="top:799px">WELCOME TO OUR WEBSITE</h2>
<div class="welcome">
  <p>Nam liber tempor cum solutia nobis eleifend option congue nihil imperdiet doming idin quod mazim placerat cer possim assum. Typi non habent claritatem insitam;est usus legentis in iis qui facit eorum claritatem. Inv igationes demonstraverunt lectores legere me lius quod ii legunt saepius.</p>
  <p>Claritas est etiam processus dynmicus, quitn sequitur mutationem consuetudium lectorumNam liber tempor um soluta nobis eleifend option congue nihil imperdiet doming id quod mazim placerat</p>
</div>

<h2 class="section-title" style="top:948px">TESTIMONIALS</h2>
<blockquote class="quote" style="left:302px">Fusce feugiat malesuada odio. Morbi nunc dograv ida &nbsp;at, cursus nec, luctus a, lorem. Maecnas tristiq ue orci acd sem. Lorem ipsum dolorsit amet.</blockquote>
<blockquote class="quote" style="left:563px">Fusce feugiat malesuada odio. Morbi nunc dograv ida &nbsp;at, cursus nec, luctus a, lorem. Maecnas tristiq ue orci acd sem. Lorem ipsum dolorsit amet.</blockquote>
<div class="author" style="left:437px"><svg width="11" height="11" viewBox="0 0 11 11"><circle cx="5.5" cy="3" r="2.7" fill="#555"/><path d="M0 11Q0 6 5.5 6T11 11Z" fill="#555"/></svg>Mara Lindqvist</div>
<div class="author" style="left:698px"><svg width="11" height="11" viewBox="0 0 11 11"><circle cx="5.5" cy="3" r="2.7" fill="#555"/><path d="M0 11Q0 6 5.5 6T11 11Z" fill="#555"/></svg>Jon Bellamy</div>

<footer class="footer">
  <div class="footer-links">Home | Products | Contact | Search | Shopping cart</div>
  <div class="footer-copy">Copyrights 2013. All Rights Reserved.</div>
  <div class="social">
    <span style="background:#3b5c9a"></span>
    <span style="background:#2b9ad6"></span>
    <span style="background:#f0701c"></span>
    <span style="background:#d4262c"></span>
  </div>
</footer>

</body>
</html>
```